Construction Company

Design a clutter free business card, it can be double-sided utilizing the logo for BDN Ltd simple with all relevant contact information.

Please also a letterhead design to function for the purposes of invoicing, all mail requirements, with header to be distinctive while the footer ties page together and incorporates all necessary information.

For now, please use generic / dummy text and when a winner is selected, I will disclose the contact information.

Hi Designers! Please read the updated brief which includes the design of a business card and letterhead. Thank you!

```html
<!DOCTYPE html>
<html lang="en">
<head>
<meta charset="utf-8">
<title>BDN Ltd Stationery</title>
<link href="https://fonts.googleapis.com/css2?family=Lato:wght@400;700;900&family=Libre+Baskerville:wght@700&display=swap" rel="stylesheet">
<style>
  :root{
    --navy:#233a8b;
    --gold:#b38f2d;
    --gold-light:#cfb064;
    --paper:#ffffff;
    --ink:#333a45;
    --muted:#8a8f98;
    --bg:#e4e5e7;
  }
  *{box-sizing:border-box;margin:0;padding:0}
  html,body{width:1200px;height:858px;overflow:hidden}
  body{background:var(--bg);font-family:"Lato",sans-serif;color:var(--ink);position:relative}
  .sheet{position:absolute;background:var(--paper);box-shadow:0 6px 18px rgba(0,0,0,.18);overflow:hidden}
  .brand{font-family:"Lato",sans-serif;font-weight:900;color:var(--navy);display:flex;align-items:center;gap:8px;letter-spacing:.5px}
  .brand-dot{border-radius:50%;background:var(--gold);flex:none}
  .brand--light{color:var(--paper)}
  .icon{width:9px;height:9px;fill:var(--navy);flex:none}
  .contact-row{display:flex;align-items:center;gap:5px}
  .band{position:absolute;left:0;bottom:0;width:100%}

  /* Letterhead */
  .letterhead{left:40px;top:50px;width:510px;height:720px}
  .letterhead .brand{position:absolute;left:42px;top:40px;font-size:30px}
  .letterhead .brand-dot{width:12px;height:12px}
  .recipient{position:absolute;left:56px;top:150px;font-size:9px;line-height:1.45;color:var(--muted)}
  .recipient strong{color:var(--ink);font-weight:700}
  .recipient .gap{margin-top:8px}
  .letter-body{position:absolute;left:56px;top:250px;width:400px;font-size:9.5px;line-height:1.6;color:var(--muted)}
  .letter-body p{margin-bottom:12px}
  .letter-body .emph{color:var(--ink);font-weight:700}
  .sign-off{position:absolute;left:56px;top:500px}
  .sign-name{font-size:13px;font-weight:700;color:var(--ink)}
  .sign-role{font-size:9px;color:var(--muted)}
  .signature{margin-top:8px;width:150px;height:40px;background:linear-gradient(90deg,rgba(35,58,139,.18),rgba(35,58,139,.06))}
  .lh-footer{position:absolute;left:56px;right:40px;bottom:54px;font-size:9px;color:var(--ink);display:flex;flex-direction:column;gap:5px}
  .lh-footer .line{display:flex;gap:16px}

  /* Business cards */
  .card{width:290px;height:166px;top:50px}
  .card-front{left:580px}
  .card-front .brand{position:absolute;left:22px;top:24px;font-size:20px}
  .card-front .brand-dot{width:8px;height:8px}
  .card-name{position:absolute;left:22px;top:72px;font-size:12px;font-weight:900;color:var(--navy)}
  .card-role{position:absolute;left:22px;top:88px;font-size:8px;font-weight:700;color:var(--gold)}
  .card-contact{position:absolute;left:22px;top:108px;font-size:7px;display:flex;flex-direction:column;gap:4px}
  .card-contact .line{display:flex;gap:10px}
  .card-back{left:890px;background:var(--navy)}
  .card-back .brand{position:absolute;left:0;right:0;top:0;bottom:0;justify-content:center;font-size:26px}
  .card-back .brand-dot{width:10px;height:10px}

  /* Compliments slip */
  .slip{left:580px;top:240px;width:290px;height:150px}
  .slip .brand{position:absolute;left:18px;top:16px;font-size:18px}
  .slip .brand-dot{width:7px;height:7px}
  .slip-contact{position:absolute;left:18px;top:44px;font-size:6.5px;display:flex;flex-direction:column;gap:3px}
  .slip-contact .icon{width:7px;height:7px}
  .slip-title{position:absolute;left:18px;bottom:26px;font-family:"Libre Baskerville",serif;font-weight:700;font-size:13px;color:var(--navy);letter-spacing:.5px}

  /* Envelope back */
  .envelope-back{left:890px;top:240px;width:290px;height:150px}
  .envelope-back svg{position:absolute;left:0;top:0}

  /* Envelope front */
  .envelope-front{left:580px;top:414px;width:600px;height:300px}
  .envelope-front .brand{position:absolute;left:40px;top:44px;font-size:36px}
  .envelope-front .brand-dot{width:14px;height:14px}
  .env-address{position:absolute;left:40px;top:102px;font-size:13px;color:var(--ink)}
  .env-contact{position:absolute;left:40px;top:130px;font-size:12px;display:flex;flex-direction:column;gap:6px}
  .env-contact .icon{width:11px;height:11px}
  .stamp-box{position:absolute;right:40px;top:40px;width:110px;height:80px;border-radius:6px;background:linear-gradient(135deg,var(--gold-light),var(--gold))}
</style>
</head>
<body>

<svg width="0" height="0" style="position:absolute" aria-hidden="true">
  <defs>
    <symbol id="i-phone" viewBox="0 0 24 24"><path d="M6.6 10.8a15.1 15.1 0 0 0 6.6 6.6l2.2-2.2c.3-.3.7-.4 1-.2 1.1.4 2.3.6 3.6.6.6 0 1 .4 1 1V20c0 .6-.4 1-1 1A17 17 0 0 1 3 4c0-.6.4-1 1-1h3.5c.6 0 1 .4 1 1 0 1.3.2 2.5.6 3.6.1.3 0 .7-.2 1z"/></symbol>
    <symbol id="i-mail" viewBox="0 0 24 24"><path d="M3 5h18v14H3z M3 5l9 7 9-7" /></symbol>
    <symbol id="i-web" viewBox="0 0 24 24"><circle cx="12" cy="12" r="10"/><path d="M2 12h20M12 2c3 3 3 17 0 20M12 2c-3 3-3 17 0 20" stroke="#fff" stroke-width="1.5" fill="none"/></symbol>
    <symbol id="i-pin" viewBox="0 0 24 24"><path d="M12 2a7 7 0 0 0-7 7c0 5 7 13 7 13s7-8 7-13a7 7 0 0 0-7-7zm0 9.5A2.5 2.5 0 1 1 12 6.5a2.5 2.5 0 0 1 0 5z"/></symbol>
  </defs>
</svg>

<!-- Letterhead -->
<section class="sheet letterhead">
  <div class="brand"><span class="brand-dot"></span>BDN Ltd</div>

  <div class="recipient">
    To:<br>
    <strong>Daniel Reeves</strong><br>
    Director
    <div class="gap"><strong>Company Name</strong><br>4120 Oakfield St,<br>Marlow, PA 16590</div>
  </div>

  <div class="letter-body">
    <p>Dear Mr.__________</p>
    <p>Lorem Ipsum is simply dummy text of the printing and typesetting industry. Lorem Ipsum has been the industry's standard dummy text ever since the 1500s, when an unknown printer took a galley of type and scrambled it to make a type specimen book. It has survived not only five centuries, but also the leap into electronic typesetting, remaining essentially unchanged. It was popularised in the 1960s with the release of Tranzline sheets containing Lorem Ipsum passages, and more recently with desktop publishing software like Pagewright Studio including versions of Lorem Ipsum.</p>
    <p class="emph">Lorem ipsum is simply dummy text of the printing and typesetting industry. Lorem ipsum has been the industry's standard dummy text ever since the 1500s.</p>
    <p>Lorem Ipsum is simply dummy text of the printing and typesetting industry.</p>
  </div>

  <div class="sign-off">
    <div class="sign-name">Your Name</div>
    <div class="sign-role">Designation</div>
    <div class="signature" role="img" aria-label="Handwritten signature"></div>
  </div>

  <div class="lh-footer">
    <div class="line"><span>27 Millbrook Rd. Harlow, PA 18420</span></div>
    <div class="line">
      <span class="contact-row"><svg class="icon"><use href="#i-phone"/></svg>+00 555-010-246</span>
      <span class="contact-row"><svg class="icon"><use href="#i-mail"/></svg>info@bdnltd.com</span>
      <span class="contact-row"><svg class="icon"><use href="#i-web"/></svg>www.bdnltd.com</span>
    </div>
  </div>

  <svg class="band" width="510" height="40" viewBox="0 0 510 40" aria-hidden="true">
    <polygon points="330,14 510,4 510,9 340,19" fill="var(--navy)"/>
    <polygon points="0,30 300,30 340,19 510,9 510,40 0,40" fill="var(--gold)"/>
  </svg>
</section>

<!-- Business card front -->
<section class="sheet card card-front">
  <div class="brand"><span class="brand-dot"></span>BDN Ltd</div>
  <div class="card-name">Your Full Name</div>
  <div class="card-role">Designation</div>
  <div class="card-contact">
    <span class="contact-row"><svg class="icon"><use href="#i-pin"/></svg>27 Millbrook Rd. Harlow, PA 18420</span>
    <div class="line">
      <span class="contact-row"><svg class="icon"><use href="#i-phone"/></svg>+00 555-010-246</span>
      <span class="contact-row"><svg class="icon"><use href="#i-mail"/></svg>info@bdnltd.com</span>
      <span class="contact-row"><svg class="icon"><use href="#i-web"/></svg>www.bdnltd.com</span>
    </div>
  </div>
  <svg class="band" width="290" height="22" viewBox="0 0 290 22" aria-hidden="true">
    <polygon points="180,6 290,0 290,4 186,10" fill="var(--navy)"/>
    <polygon points="0,14 160,14 186,10 290,4 290,22 0,22" fill="var(--gold)"/>
  </svg>
</section>

<!-- Business card back -->
<section class="sheet card card-back">
  <div class="brand brand--light"><span class="brand-dot"></span>BDN Ltd</div>
</section>

<!-- Compliments slip -->
<section class="sheet slip">
  <div class="brand"><span class="brand-dot"></span>BDN Ltd</div>
  <div class="slip-contact">
    <span>27 Millbrook Rd. Harlow, PA 18420</span>
    <span class="contact-row"><svg class="icon"><use href="#i-phone"/></svg>+00 555-010-246</span>
    <span class="contact-row"><svg class="icon"><use href="#i-mail"/></svg>info@bdnltd.com</span>
    <span class="contact-row"><svg class="icon"><use href="#i-web"/></svg>www.bdnltd.com</span>
  </div>
  <div class="slip-title">WITH COMPLIMENTS</div>
  <svg class="band" width="290" height="22" viewBox="0 0 290 22" aria-hidden="true">
    <polygon points="160,8 290,0 290,4 168,12" fill="var(--navy)"/>
    <polygon points="0,16 140,16 168,12 290,4 290,22 0,22" fill="var(--gold)"/>
  </svg>
</section>

<!-- Envelope back -->
<section class="sheet envelope-back" aria-label="Envelope back">
  <svg width="290" height="150" viewBox="0 0 290 150" aria-hidden="true">
    <polyline points="0,150 145,80 290,150" fill="none" stroke="#e6e7ea" stroke-width="1"/>
    <path d="M0 0 H290 V48 Q290 58 280 60 L10 60 Q0 58 0 48 Z" fill="var(--navy)"/>
  </svg>
</section>

<!-- Envelope front -->
<section class="sheet envelope-front">
  <div class="brand"><span class="brand-dot"></span>BDN Ltd</div>
  <div class="env-address">27 Millbrook Rd. Harlow, PA 18420</div>
  <div class="env-contact">
    <span class="contact-row"><svg class="icon"><use href="#i-phone"/></svg>+00 555-010-246</span>
    <span class="contact-row"><svg class="icon"><use href="#i-mail"/></svg>info@bdnltd.com</span>
    <span class="contact-row"><svg class="icon"><use href="#i-web"/></svg>www.bdnltd.com</span>
  </div>
  <div class="stamp-box"></div>
  <svg class="band" width="600" height="36" viewBox="0 0 600 36" aria-hidden="true">
    <polygon points="380,14 600,2 600,8 392,20" fill="var(--navy)"/>
    <polygon points="0,26 350,26 392,20 600,8 600,36 0,36" fill="var(--gold)"/>
  </svg>
</section>

</body>
</html>
```